Love Your Hearing - Life Sounds Good

I need a website. I had a company doing it, and it looked very nice, but they went way up on hosting costs and said they owned the design of the site. I changed hosts to keep costs down. You can see the current design at crestvaleaudio.com. They said I could use the copy and images from the current website. So you could cut and paste to speed things up. My logo and other images are on the current website. If you are unable to use I can send other digital copies.

Target Market(s)

seniors 55 and up

Number of Pages Required

4 page

Font styles to use
Sans Serif

Colors
0255a3
f78f20

Requirements
Must have
• Video testimonies that I can add without assistance. I use youtube links for the videos.
Nice to have
• The color scheme theme can be drawn from the logo, which is on the current webstie crestvaleaudio.com
Should not have
• Should not have anything related to SonoPath on the website.

```html
<!DOCTYPE html>
<html lang="en">
<head>
<meta charset="utf-8">
<title>Crestvale Hearing Center</title>
<link href="https://fonts.googleapis.com/css2?family=Raleway:wght@400;500;600;700&family=Lato:wght@300;400;700&display=swap" rel="stylesheet">
<style>
:root{
  --blue:#0255a3;
  --blue-deep:#064a92;
  --orange:#f78f20;
  --orange-deep:#df7a25;
  --ink:#333;
  --muted:#9a9a9a;
  --dark:#2b2b2b;
  --darker:#222;
  --white:#fff;
}
*{box-sizing:border-box;margin:0;padding:0}
html,body{width:1200px;height:4594px;overflow:hidden;background:var(--white)}
body{font-family:'Lato',sans-serif;color:var(--ink);position:relative}
section,header,nav,footer,.topbar{position:relative;width:1200px;overflow:hidden}
h1,h2,h3,h4{font-family:'Raleway',sans-serif;font-weight:500}

/* top bar */
.topbar{height:30px;background:var(--darker);color:#ddd;font-size:11px;display:flex;align-items:center;justify-content:space-between;padding:0 112px 0 120px}
.topbar .follow{display:flex;align-items:center;gap:9px}
.dot{width:8px;height:8px;border-radius:50%;background:#ddd;display:inline-block}

/* header */
.site-header{height:120px;display:flex;align-items:center;justify-content:space-between;padding:0 106px 0 118px}
.brand{display:flex;align-items:center;gap:10px}
.brand-mark{width:48px;height:48px;background:var(--orange)}
.brand-name{font-family:'Raleway',sans-serif;font-weight:700;color:var(--blue);font-size:22px;line-height:1.05}
.contacts{display:flex;align-items:center;gap:28px;font-size:11px}
.contact{display:flex;align-items:center;gap:8px}
.contact b{font-family:'Raleway',sans-serif;color:var(--blue);font-size:18px;font-weight:500}
.divider{width:1px;height:26px;background:#ccc}

/* nav */
.main-nav{height:55px;background:var(--blue);display:flex;align-items:center;padding:0 100px 0 124px;color:#fff;font-family:'Raleway',sans-serif;font-size:11px;font-weight:600}
.main-nav ul{display:flex;list-style:none;gap:0}
.main-nav li{margin-right:54px}
.btn-appt{margin-left:auto;background:var(--orange);color:#fff;padding:11px 16px;font-size:11px}

/* hero */
.hero{height:633px}
.hero-photo{position:absolute;inset:0;background:linear-gradient(120deg,#c9dbe4 0%,#e6ecee 40%,#d9dfe2 70%,#b9c6cc 100%)}
.hero-tag{position:absolute;left:110px;color:#fff;font-family:'Raleway',sans-serif;font-weight:600;padding:0 20px;display:flex;align-items:center}
.hero-tag.one{top:501px;height:64px;width:528px;background:var(--orange);font-size:29px}
.hero-tag.two{top:570px;height:67px;width:744px;background:var(--blue);font-size:29px}
.hero-btn{position:absolute;left:110px;top:674px;width:207px;height:52px;background:var(--orange-deep);color:#fff;font-size:15px;display:flex;align-items:center;justify-content:center}
.arrow-circle{position:absolute;width:58px;height:58px;border-radius:50%;background:rgba(40,40,40,.7);display:flex;align-items:center;justify-content:center}
.hero .arrow-circle{top:281px}
.hero .arrow-circle.left{left:23px}.hero .arrow-circle.right{left:1118px}

/* about */
.about{height:503px}
.about-text{position:absolute;left:110px;top:120px;width:590px}
.about-text h2{font-size:40px;color:#222}
.about-text h3{font-size:28px;margin:18px 0 28px;color:#333}
.about-text p{font-family:'Lato',sans-serif;font-weight:300;font-size:16.5px;line-height:30px;color:#888}
.btn-blue{display:inline-block;background:var(--blue);color:#fff;font-family:'Raleway',sans-serif;font-size:11px;font-weight:600;text-align:center;line-height:36px}
.about .btn-blue{margin-top:28px;width:148px}
.about-photo{position:absolute;left:726px;top:66px;width:474px;height:378px;background:linear-gradient(135deg,#e9f0f5,#cfe0ee 55%,#9fc3df)}

/* feature */
.feature{height:533px;background:var(--orange-deep);color:#fff}
.feature-photo{position:absolute;left:112px;top:109px;width:489px;height:324px;border-radius:6px;background:linear-gradient(135deg,#f4efe9,#e9d6c8 55%,#d4b8a3)}
.feature-text{position:absolute;left:667px;top:100px}
.feature-text h2{font-size:31px;font-weight:500}
.byline{font-size:10px;margin:28px 0 18px;font-weight:700}
.feature-text ul{list-style:none;margin-left:16px}
.feature-text li{font-size:14px;line-height:41px;display:flex;align-items:center;gap:12px}
.feature-text li::before{content:"";width:6px;height:6px;border-radius:50%;background:#fff}
.feature .btn-blue{margin:14px 0 0 14px;width:148px}

/* services */
.services{height:767px;text-align:center}
.section-title{font-size:32px;color:#333}
.section-sub{font-weight:300;color:#a0a0a0;font-size:17px;margin-top:8px}
.services .section-title{padding-top:96px}
.service-grid{position:absolute;left:0;top:250px;width:1200px;display:grid;grid-template-columns:repeat(3,324px);justify-content:center;row-gap:100px}
.service svg{width:64px;height:64px}
.service h4{font-size:15px;margin:18px 0 14px;color:#333;font-family:'Lato',sans-serif;font-weight:400}
.service p{font-size:11px;color:#888;line-height:20px}

/* testimonials */
.testimonials{height:585px;background:var(--blue);color:#fff;text-align:center}
.testimonials h2{font-size:32px;padding-top:78px}
.testimonials .lede{font-size:18px;margin-top:22px;font-family:'Raleway',sans-serif}
.video{position:absolute;left:280px;top:191px;width:640px;height:324px;border-radius:4px;background:linear-gradient(120deg,#e9eef2,#cbd6de 55%,#b8c4cc)}
.play{position:absolute;left:285px;top:127px;width:70px;height:70px;border-radius:50%;background:var(--orange);display:flex;align-items:center;justify-content:center}
.testimonials .arrow-circle{top:311px;background:rgba(255,255,255,.35)}
.testimonials .arrow-circle.left{left:71px}.testimonials .arrow-circle.right{left:1087px}

/* newsletter */
.newsletter{height:198px;background:var(--orange);color:#fff}
.newsletter-text{position:absolute;left:112px;top:60px}
.newsletter-text h3{font-size:24px}
.newsletter-text p{font-size:14px;line-height:24px;margin-top:6px}
.subscribe{position:absolute;left:658px;top:66px;width:438px;height:40px;background:#fff;border-radius:20px;border:3px solid #fff;display:flex;align-items:center}
.subscribe span{flex:1;color:#999;font-size:11px;padding-left:28px}
.subscribe b{width:170px;height:34px;border-radius:17px;background:var(--blue);color:#fff;font-size:11px;display:flex;align-items:center;justify-content:center;font-weight:700}

/* articles */
.articles{height:700px;text-align:center}
.articles .section-title{padding-top:98px}
.articles .section-sub{color:#666;font-weight:400;font-size:18px;margin-top:14px}
.cards{position:absolute;left:109px;top:244px;display:flex;gap:8px}
.card{width:322px;height:349px;background:var(--blue);color:#fff;text-align:left;display:flex;flex-direction:column}
.card-photo{height:175px}
.card:nth-child(1) .card-photo{background:linear-gradient(135deg,#e4ded5,#b49a82)}
.card:nth-child(2) .card-photo{background:linear-gradient(135deg,#d85f8a,#f0b45a 60%,#6a9e4a)}
.card:nth-child(3) .card-photo{background:linear-gradient(135deg,#dfe4e6,#c4b6a6)}
.card-body{padding:20px 20px 0;flex:1}
.card h4{font-family:'Lato',sans-serif;font-size:14px;line-height:18px;font-weight:400}
.card p{font-size:10px;line-height:19px;margin-top:10px}
.card-foot{margin:0 10px;border-top:1px solid rgba(255,255,255,.35);height:38px;display:flex;align-items:center;justify-content:space-between;padding:0 10px;font-size:10px;font-weight:700}

/* footer */
.site-footer{height:470px;background:var(--dark);color:#ccc}
.footer-cols{position:absolute;left:109px;top:112px;display:flex}
.footer-col h5{font-family:'Raleway',sans-serif;font-size:12px;color:#fff;font-weight:600;margin-bottom:26px}
.footer-col li{list-style:none;font-size:12px;line-height:15px;margin-bottom:17px}
.copyright{position:absolute;top:422px;width:1200px;text-align:center;font-size:11px}
</style>
</head>
<body>

<div class="topbar">
  <span>&#9678; 48 Alder Row, Suite 7, Crestvale, NC 28090</span>
  <span class="follow">Follow Us: <i class="dot"></i><i class="dot"></i><i class="dot"></i></span>
</div>

<header class="site-header">
  <div class="brand"><span class="brand-mark"></span><span class="brand-name">CRESTVALE<br>HEARING CENTER</span></div>
  <div class="contacts">
    <div class="contact">
      <svg width="20" height="14" viewBox="0 0 20 14"><rect x="1" y="1" width="18" height="12" fill="none" stroke="#f78f20" stroke-width="1.5"/><path d="M1 1l9 7 9-7" fill="none" stroke="#f78f20" stroke-width="1.5"/></svg>
      Mail us! <b>hello@crestvaleaudio.com</b>
    </div>
    <span class="divider"></span>
    <div class="contact">
      <svg width="14" height="20" viewBox="0 0 14 20"><rect x="1" y="1" width="12" height="18" rx="2" fill="none" stroke="#f78f20" stroke-width="1.5"/><circle cx="7" cy="15" r="1.2" fill="#f78f20"/></svg>
      Call us! <b>(555) 014-2290</b>
    </div>
  </div>
</header>

<nav class="main-nav">
  <ul><li>HOME &#8964;</li><li>HEARING AIDS</li><li>OUR SERVICES</li><li>EDUCATION</li><li>ABOUT US</li><li>CONTACT</li></ul>
  <span class="btn-appt">BOOK AN APPOINTMENT</span>
</nav>

<section class="hero">
  <div class="hero-photo" role="img" aria-label="Photo of a young girl whispering into her smiling grandmother's ear in a kitchen"></div>
  <div class="arrow-circle left"><svg width="14" height="14" viewBox="0 0 14 14"><path d="M9 2L4 7l5 5" fill="none" stroke="#fff" stroke-width="1.5"/></svg></div>
  <div class="arrow-circle right"><svg width="14" height="14" viewBox="0 0 14 14"><path d="M5 2l5 5-5 5" fill="none" stroke="#fff" stroke-width="1.5"/></svg></div>
  <div class="hero-tag one">RECAPTURE THE SOUNDS OF LIFE</div>
  <div class="hero-tag two">AND THE INTIMACY OF A QUIET CONVERSATION</div>
  <div class="hero-btn">Take Action Today</div>
</section>

<section class="about">
  <div class="about-text">
    <h2>ABOUT US</h2>
    <h3>Welcome to Crestvale Hearing Center LLC</h3>
    <p>We provide hearing evaluations, counseling, and fitting of hearing aids. We service all the major brands of hearing aids including Aurelo, Tonwell, Veramic, Lindor, Quellin, Harbex, Nexaud, Sonteq, Clarivo, Mellon, Audrex, and others.</p>
    <span class="btn-blue">READ MORE</span>
  </div>
  <div class="about-photo" role="img" aria-label="Photo of a nurse in gloves examining a patient's neck"></div>
</section>

<section class="feature">
  <div class="feature-photo" role="img" aria-label="Photo of a woman touching her ear with eyes closed"></div>
  <div class="feature-text">
    <h2>50 Ways to Love Your Hearing</h2>
    <p class="byline">by Warren Ames</p>
    <ul><li>Bi-Annual Hearing Checkups</li><li>20 db Hearing or Better</li><li>Quiet Conversation</li><li>Music</li><li>Dancing</li></ul>
    <span class="btn-blue">READ MORE</span>
  </div>
</section>

<section class="services">
  <h2 class="section-title">How can we help you?</h2>
  <p class="section-sub">Lorem ipsum dolor sit amet, consectetur adipisicing elit, sed</p>
  <div class="service-grid">
    <div class="service">
      <svg viewBox="0 0 64 64" fill="none" stroke="#0255a3" stroke-width="2.5"><path d="M20 26a14 14 0 0 1 28 0c0 8-8 10-8 18a8 8 0 0 1-14 4"/><path d="M28 26a6 6 0 0 1 12 0c0 4-4 5-4 9"/><path d="M50 10l-6 6M18 54l-6 6"/></svg>
      <h4>Hearing Aids</h4><p>Lorem ipsum dolor sit amet, consectetur<br>adipisicing elit, sed do eiusmod tempor</p>
    </div>
    <div class="service">
      <svg viewBox="0 0 64 64" fill="none" stroke="#0255a3" stroke-width="2.5"><circle cx="30" cy="20" r="9"/><path d="M12 56V46a18 10 0 0 1 36 0v10z"/><rect x="46" y="22" width="8" height="14"/></svg>
      <h4>Tinnitus Treatmen</h4><p>Lorem ipsum dolor sit amet, consectetur<br>adipisicing elit, sed do eiusmod tempor</p>
    </div>
    <div class="service">
      <svg viewBox="0 0 64 64" fill="none" stroke="#0255a3" stroke-width="2.5"><path d="M12 40V30a20 20 0 0 1 40 0v10"/><rect x="8" y="34" width="10" height="18" rx="4"/><rect x="46" y="34" width="10" height="18" rx="4"/><path d="M26 34h4l5-5v16l-5-5h-4zM39 33a6 6 0 0 1 0 8"/></svg>
      <h4>Ear Molds (Protection)</h4><p>Lorem ipsum dolor sit amet, consectetur<br>adipisicing elit, sed do eiusmod tempor</p>
    </div>
    <div class="service">
      <svg viewBox="0 0 64 64"><path d="M32 6a24 24 0 1 0 0 48l-4 8 12-10A24 24 0 0 0 32 6z" fill="#0255a3"/><text x="32" y="40" text-anchor="middle" font-family="Lato,sans-serif" font-weight="700" font-size="28" fill="#fff">?</text></svg>
      <h4>F.A.Q.</h4><p>Lorem ipsum dolor sit amet, consectetur<br>adipisicing elit, sed do eiusmod tempor</p>
    </div>
    <div class="service">
      <svg viewBox="0 0 64 64" fill="none" stroke="#0255a3" stroke-width="2.5"><path d="M22 30a10 10 0 1 1 20 0c0 6-5 8-5 14H27c0-6-5-8-5-14z"/><path d="M27 48h10M28 53h8M32 6v6M12 14l4 4M52 14l-4 4M6 30h6M52 30h6"/></svg>
      <h4>Tips for Wearers</h4><p>Lorem ipsum dolor sit amet, consectetur<br>adipisicing elit, sed do eiusmod tempor</p>
    </div>
    <div class="service">
      <svg viewBox="0 0 64 64" fill="none" stroke="#0255a3" stroke-width="2.5"><rect x="8" y="12" width="48" height="44" rx="3"/><path d="M8 22h48M18 6v10M46 6v10"/><circle cx="18" cy="32" r="2.5"/><circle cx="28" cy="32" r="2.5"/><circle cx="38" cy="32" r="2.5"/><circle cx="48" cy="32" r="2.5"/><circle cx="28" cy="44" r="2.5"/><circle cx="38" cy="44" r="2.5"/><path d="M14 44l3 3 5-6"/></svg>
      <h4>Schedule an Appointment</h4><p>Lorem ipsum dolor sit amet, consectetur<br>adipisicing elit, sed do eiusmod tempor</p>
    </div>
  </div>
</section>

<section class="testimonials">
  <h2>What Our Client Says!</h2>
  <p class="lede">Lorem ipsum dolor sit amet, consectetur adipisicing</p>
  <div class="arrow-circle left"><svg width="14" height="14" viewBox="0 0 14 14"><path d="M9 2L4 7l5 5" fill="none" stroke="#fff" stroke-width="1.5"/></svg></div>
  <div class="arrow-circle right"><svg width="14" height="14" viewBox="0 0 14 14"><path d="M5 2l5 5-5 5" fill="none" stroke="#fff" stroke-width="1.5"/></svg></div>
  <div class="video" role="img" aria-label="Video thumbnail of a doctor examining an older woman's ear">
    <div class="play"><svg width="26" height="28" viewBox="0 0 26 28"><path d="M4 2l20 12L4 26z" fill="#fff"/></svg></div>
  </div>
</section>

<section class="newsletter">
  <div class="newsletter-text">
    <h3>What's New in Hearing Health?</h3>
    <p>Learn more about hearing healthcare through the articles below;<br>click here to subscribe.</p>
  </div>
  <div class="subscribe"><span>Your Email Address Here ...</span><b>SUSCRIBE</b></div>
</section>

<section class="articles">
  <h2 class="section-title">Articles</h2>
  <p class="section-sub">Stay updated with recent events, news &amp; tips from us!</p>
  <div class="cards">
    <article class="card">
      <div class="card-photo" role="img" aria-label="Photo of a young man helping an older man"></div>
      <div class="card-body"><h4>Do's and Don'ts for<br>Communicating During the</h4><p>It's important to make sure that everyone is comfortable and getting what they need in large group settings, and using these tips ...</p></div>
      <div class="card-foot"><span>READ MORE</span><span>&#9638; DECEMBER 19, 2018</span></div>
    </article>
    <article class="card">
      <div class="card-photo" role="img" aria-label="Photo of a smiling child in a flower garden"></div>
      <div class="card-body"><h4>Communication for All: How People of All Ages Benefit from Better Hearing and Communication</h4><p>Regardless of age, occupation or gender everyone can benefit from clear communication ...</p></div>
      <div class="card-foot"><span>READ MORE</span><span>&#9638; JANUARY 06, 2019</span></div>
    </article>
    <article class="card">
      <div class="card-photo" role="img" aria-label="Photo of a smiling older couple"></div>
      <div class="card-body"><h4>Over-the-Counter Hearing<br>Aids: What You Need to Know</h4><p>In August 2017, a law was passed that allows FDA-regulated hearing aids to be sold over the counter instead ...</p></div>
      <div class="card-foot"><span>READ MORE</span><span>&#9638; SEPTEMBER 14, 2017</span></div>
    </article>
  </div>
</section>

<footer class="site-footer">
  <div class="footer-cols">
    <div class="footer-col" style="width:163px"><h5>HOME</h5><ul><li>Welcome</li><li>Healthcare News</li></ul></div>
    <div class="footer-col" style="width:163px"><h5>ABOUT US</h5><ul><li>Meet The Specialist</li><li>Video Testimonials</li></ul></div>
    <div class="footer-col" style="width:191px"><h5>THE SERVICES</h5><ul><li>Tinnitus Treatment</li><li>Insurance &amp; Financing<br>Info</li></ul></div>
    <div class="footer-col" style="width:160px"><h5>CONTACT</h5><ul><li>Location And Map</li><li>New Patient Forms</li><li>Links</li></ul></div>
    <div class="footer-col" style="width:184px"><h5>HEARING AIDS</h5><ul><li>Brands</li><li>Repairs / Maintenance</li><li>Batteries</li><li>Featured Technology</li></ul></div>
    <div class="footer-col" style="width:130px"><h5>EDUCATION</h5><ul><li>Hearing Myths</li><li>Frequently Asked<br>Questions</li><li>Tips For Hearing Aid<br>Wearers And Family<br>Members</li></ul></div>
  </div>
  <p class="copyright">(C) 2019 Crestvale Hearing Center LLC Healthcare</p>
</footer>

</body>
</html>
```